Business Cards + Flyer + Letterhead for Care Recruitment Agency

We are a recruitment agency for the health & care sector. We need designs made for business cards, A5 double-sided flyer, and a letterhead template.

Our branding message is professionalism, care, compassion, expertise. We are experts in recruitment for the care & health industry.

Our logo source files and colours are here - https://www.fileporta.net/sh/qrvn82lopx4kdte/BBBgKy8LMQ27uTnPwZxHcVobsa?dl=0

For the business card, I have attached an example we like. We want a vertical business card design, something very similar to the example given. The design should match our logo in terms of brand colors. On one side should be our logo, our website (www.hollowmere.co.uk) and Care Recruitment Specialists written somewhere visible that fits, between our logo and the website at the bottom. On the other side should be our details.

Details on the front:

Logo with slogan
Care Recruitment Specialists
www.hollowmere.co.uk

Details on the back:

Tobias Orlund
Managing Director

Pellam House, 31-39 Larkfield St, Birmingham, B4 7QD
07612 495371
tobias@hollowmere.co.uk
www.hollowmere.co.uk

Marnie Holloway
Business Development Director

07831 204968
marnie@hollowmere.co.uk
www.hollowmere.co.uk

For the A5 flyer, I have attached some pictures we've used for the website, which could be used for the flyer as well. To get a better idea of our branding, please visit our website - https://hollowmere.co.uk/

The text for the flyer is also attached.

Finally, the letterhead template should be a docx template with our logo and our identifiable branding (the same shapes and matching colours you will come up with for the business cards and flyer).

```html
<!DOCTYPE html>
<html lang="en">
<head>
<meta charset="utf-8">
<title>Hollowmere – A5 Brochure Spreads</title>
<link rel="stylesheet" href="https://fonts.googleapis.com/css2?family=Lato:ital,wght@0,400;0,700;0,900;1,400&display=swap">
<style>
  :root {
    --navy: #1b2a57;
    --navy-deep: #16224a;
    --royal: #1f5fa8;
    --bright: #2a8fd4;
    --sky: #4fb0e6;
    --steel: #3d6797;
    --steel-dark: #2c4f7c;
    --ink: #4a4f5a;
    --paper: #ffffff;
    --backdrop: #e9e8e5;
    --photo-warm: #c9b7a4;
    --photo-cool: #b9d3e4;
    --photo-green: #9fb89a;
  }
  * { box-sizing: border-box; margin: 0; padding: 0; }
  html, body { width: 1200px; height: 840px; overflow: hidden; }
  body {
    background: var(--backdrop);
    font-family: "Lato", sans-serif;
    color: var(--ink);
    position: relative;
  }
  .spread {
    position: absolute;
    top: 215px;
    width: 580px;
    height: 410px;
    display: flex;
    box-shadow: 0 6px 18px rgba(0,0,0,.12);
  }
  .spread--outer { left: 10px; }
  .spread--inner { left: 610px; }
  .page {
    position: relative;
    width: 290px;
    height: 410px;
    background: var(--paper);
    overflow: hidden;
  }
  .page + .page { border-left: 1px solid rgba(0,0,0,.06); }
  .page svg.shape { position: absolute; left: 0; top: 0; width: 290px; height: 410px; }
  .photo { position: absolute; }

  /* back cover */
  .back-title {
    position: absolute; left: 20px; top: 26px; width: 250px;
    color: var(--bright); font-weight: 900; font-size: 17px; line-height: 1.15;
  }
  .back-photo { right: 20px; top: 82px; width: 88px; height: 78px;
    background: linear-gradient(135deg, var(--photo-cool), #e6eef4 60%, var(--photo-warm)); }
  .back-copy {
    position: absolute; left: 20px; top: 84px; width: 155px;
    font-size: 6.6px; line-height: 1.45;
  }
  .back-sign {
    position: absolute; left: 20px; top: 192px;
    color: var(--bright); font-weight: 700; font-size: 9px;
  }
  .back-contact {
    position: absolute; left: 22px; bottom: 26px;
    color: var(--sky); font-weight: 700; font-size: 9px; line-height: 1.35;
  }

  /* front cover */
  .cover-photo { left: 40px; top: 0; width: 250px; height: 150px;
    background: linear-gradient(120deg, var(--photo-green), #d7cfc4 45%, var(--photo-warm)); }
  .brand {
    position: absolute; left: 58px; top: 214px;
    display: flex; align-items: center; gap: 8px;
  }
  .brand-dot { width: 20px; height: 20px; border-radius: 50%; background: var(--bright); }
  .brand-name { color: var(--navy); font-weight: 700; font-size: 18px; line-height: 1; }
  .cover-web {
    position: absolute; right: 26px; bottom: 36px;
    color: var(--sky); font-weight: 700; font-size: 9px;
  }

  /* inside left */
  .hands-photo { left: 0; top: 0; width: 290px; height: 175px;
    background: linear-gradient(160deg, #e9ece6, var(--photo-green) 45%, #efe7dd 80%); }
  .why-title {
    position: absolute; left: 20px; top: 188px;
    color: var(--bright); font-weight: 900; font-size: 13px;
  }
  .col {
    position: absolute; top: 210px; width: 120px;
    font-size: 5.6px; line-height: 1.42; text-align: justify;
  }
  .col--a { left: 20px; }
  .col--b { left: 150px; top: 184px; }
  .stat {
    position: absolute; left: 150px; top: 300px; width: 120px;
    color: var(--royal); font-weight: 900; font-size: 9.5px; line-height: 1.2;
  }

  /* inside right */
  .stick-photo { left: 0; top: 0; width: 290px; height: 120px;
    background: linear-gradient(110deg, var(--photo-cool), #d9c4a0 55%, var(--photo-green)); }
  .carer-photo { right: 22px; top: 134px; width: 88px; height: 72px;
    background: linear-gradient(135deg, var(--photo-cool), #eef2f6 55%, var(--photo-warm)); }
  .partner-copy {
    position: absolute; left: 20px; top: 134px; width: 152px;
    font-size: 5.9px; line-height: 1.45; text-align: justify;
  }
  .partner-copy p + p { margin-top: 4px; }
</style>
</head>
<body>

<section class="spread spread--outer">
  <article class="page page--back">
    <svg class="shape" viewBox="0 0 290 410" aria-hidden="true">
      <defs>
        <linearGradient id="steelFade" x1="0" y1="0" x2="1" y2="1">
          <stop offset="0" stop-color="var(--steel)"/>
          <stop offset="1" stop-color="var(--steel-dark)"/>
        </linearGradient>
      </defs>
      <path d="M0 268 C90 250 190 236 290 222 L290 410 L0 410 Z" fill="var(--sky)"/>
      <path d="M0 276 C90 258 190 244 290 230 L290 410 L0 410 Z" fill="url(#steelFade)"/>
    </svg>
    <h2 class="back-title">What value can Hollowmere add to your business?</h2>
    <div class="photo back-photo" role="img" aria-label="Photo of a carer talking with an elderly resident"></div>
    <p class="back-copy">We understand Care operators are time poor. Advertising the role is one thing, but finding the time to trawl through the responses, make a shortlist, call to arrange interviews, carry out interviews and all the other ancillary tasks associated with hiring staff… it can feel overwhelming! We are here to support and help Care operators and candidates every step of the way.</p>
    <p class="back-sign">We couldn’t care more.</p>
    <p class="back-contact">Call Us: 0121 604 3317 or 07418 662094<br>Or email us to book a call at contact@hollowmere.co.uk<br>www.hollowmere.co.uk</p>
  </article>

  <article class="page page--front">
    <div class="photo cover-photo" role="img" aria-label="Photo of a smiling carer with an elderly woman"></div>
    <svg class="shape" viewBox="0 0 290 410" aria-hidden="true">
      <path d="M0 330 C120 318 230 250 290 150 L290 410 L0 410 Z" fill="var(--bright)"/>
      <path d="M0 342 C130 330 235 262 290 172 L290 410 L0 410 Z" fill="var(--royal)"/>
      <path d="M0 356 C140 346 240 280 290 196 L290 410 L0 410 Z" fill="var(--navy)"/>
    </svg>
    <div class="brand">
      <span class="brand-dot"></span>
      <span class="brand-name">Hollowmere</span>
    </div>
    <p class="cover-web">www.hollowmere.co.uk</p>
  </article>
</section>

<section class="spread spread--inner">
  <article class="page page--why">
    <div class="photo hands-photo" role="img" aria-label="Photo of a young hand holding an elderly hand"></div>
    <svg class="shape" viewBox="0 0 290 410" aria-hidden="true">
      <path d="M0 180 L0 175 C90 170 180 150 290 120 L290 180 Z" fill="var(--paper)"/>
    </svg>
    <h2 class="why-title">Why Hollowmere?</h2>
    <p class="col col--a">Almost 20 years ago we commenced our journey in the Health and Social Care space. During this time, we have experienced the highs and not-so-highs of this wonderful sector, working with Residential Care providers, home care, NHS Hospitals, Local Authorities, Housing, Adult Education, Early Years settings and Schools. We recognise the operational challenges experienced by every organisation within the Health and Social Care space. Staffing and Recruitment is one of the biggest challenges. It takes huge amounts of time, which Care operators do not have, and it is vital they have enough time to focus on delivering exceptional care and ensuring the quality of service. We decided to create Hollowmere to channel all of our experience into forming valuable partnerships with Care operators to alleviate some of the pressure they face.</p>
    <p class="col col--b">organisations are experiencing when it comes to recruiting staff, effectively reducing their time to ensure best practices are upheld and the new staff members are happy and supported, most importantly that they stay in post long term. We have a proven track record of working with Care organisations of various sizes and making a big impact on the cost per hire for each new member of staff, along with reducing use of casual agency staff to cover unfilled vacancies.</p>
    <p class="stat">In fact… in one large multi-site operation, our permanent recruitment methods reduced temporary agency spend by a whopping 85%.</p>
  </article>

  <article class="page page--partner">
    <div class="photo stick-photo" role="img" aria-label="Photo of a carer's hand resting on an elderly person's hand on a walking stick"></div>
    <div class="photo carer-photo" role="img" aria-label="Photo of a carer talking with an elderly resident"></div>
    <div class="partner-copy">
      <p>We want to create a genuine and long lasting partnership. You have our word that we will strive to work in close collaboration with you to devise and implement a recruitment strategy that will enable and empower Care operator teams to plan for staff turnover and business growth.</p>
      <p>We leave no stone unturned in our quest to recruit the very best talent out there in the workforce. We never headhunt, but we go above and beyond just chucking out an advert and hoping for the best candidates to come to us.</p>
      <p>We provide ongoing support to our clients and share our experience on combating high staff turnover and low staff morale.</p>
      <p>So, why not give us a try? We want to permanently place the best candidates in the best Care settings and we will stop at nothing to make it happen!</p>
    </div>
    <svg class="shape" viewBox="0 0 290 410" aria-hidden="true">
      <path d="M290 190 C265 260 225 330 150 410 L290 410 Z" fill="var(--sky)"/>
      <path d="M290 214 C268 280 232 345 172 410 L290 410 Z" fill="var(--bright)"/>
      <path d="M290 250 C272 305 248 355 206 410 L290 410 Z" fill="var(--royal)"/>
      <path d="M290 300 C280 340 262 378 240 410 L290 410 Z" fill="var(--navy)"/>
    </svg>
  </article>
</section>

</body>
</html>
```